Need Letterhead Design & Matching Business Card

I have a logo that I love already. But the letterhead is less than appealing and boring. I'd like a design for my letterhead which I will match with business cards. Also, I'd like to have used fonts that are generally available, as my current letterhead uses a font named "SPACE" which nobody has unless they download it...so when a Word version is forwarded, it looks awful on the receiver's screed due to not having the font. That being said, modern is the look we like and are going for.

My business is "Halloran Brightmoor PC" - a law firm specializing in representing people who have suffered catastrophic injuries or death (plane, auto, train crashes etc.).

See attached letterhead, which has all of the pertinent information. My logo is also attached in various formats.

```html
<!DOCTYPE html>
<html lang="en">
<head>
<meta charset="utf-8">
<title>Halloran Brightmoor PC — Business Card</title>
<link rel="stylesheet" href="https://fonts.googleapis.com/css2?family=Montserrat:wght@300;400;600;700&family=Source+Sans+3:wght@400;600&display=swap">
<style>
  :root {
    --backdrop: #b6b6b6;
    --card-dark: #2b2929;
    --card-light: #f4f4f4;
    --ink-dark: #262424;
    --ink-light: #ffffff;
  }
  * { margin: 0; padding: 0; box-sizing: border-box; }
  html, body { width: 1200px; height: 900px; overflow: hidden; }
  body { background: var(--backdrop); position: relative; font-family: "Montserrat", sans-serif; }

  .card { position: absolute; width: 412px; height: 234px; }
  .card * { position: absolute; line-height: 1; white-space: nowrap; }

  /* Front */
  .card--front { left: 392px; top: 196px; background: var(--card-dark); color: var(--ink-light); }
  .card--front .accent-rule { left: 0; top: 50px; width: 35px; height: 1px; background: var(--ink-light); }
  .card--front .mark-square { left: 322px; top: 50px; width: 41px; height: 41px; background: var(--ink-light); }
  .card--front .wordmark { left: 52px; top: 144px; font-weight: 300; font-size: 18.5px; letter-spacing: 3.4px; line-height: 25px; white-space: normal; }
  .card--front .web { left: 268px; top: 177px; font-weight: 700; font-size: 6px; letter-spacing: 0.1px; }

  /* Back */
  .card--back { left: 396px; top: 496px; background: var(--card-light); color: var(--ink-dark); }
  .card--back .accent-rule { left: 0; top: 36px; width: 28px; height: 1px; background: var(--ink-dark); }
  .card--back .wordmark { left: 35px; top: 34px; font-weight: 400; font-size: 12.5px; letter-spacing: 2.4px; line-height: 17.5px; white-space: normal; }
  .card--back .mark-square { left: 332px; top: 35px; width: 33px; height: 33px; background: var(--ink-dark); }
  .card--back .person-name { left: 34px; top: 100px; font-weight: 700; font-size: 16px; }
  .card--back .person-title { left: 35px; top: 119px; font-weight: 400; font-size: 8.5px; }
  .contact { font-family: "Source Sans 3", sans-serif; font-size: 8.3px; line-height: 12.8px; top: 163px; }
  .contact span { position: static; display: block; }
  .contact .firm { font-weight: 600; }
  .contact--address { left: 34px; }
  .contact--reach { left: 244px; }
</style>
</head>
<body>
  <section class="card card--front" aria-label="Business card front">
    <div class="accent-rule"></div>
    <div class="mark-square"></div>
    <h1 class="wordmark">HALLORAN<br>BRIGHTMOOR</h1>
    <p class="web">www.halloranbrightmoor.com</p>
  </section>

  <section class="card card--back" aria-label="Business card back">
    <div class="accent-rule"></div>
    <h2 class="wordmark">HALLORAN<br>BRIGHTMOOR</h2>
    <div class="mark-square"></div>
    <p class="person-name">R. Daniel Okafor</p>
    <p class="person-title">Founder and President</p>
    <address class="contact contact--address">
      <span class="firm">Halloran Brightmoor PC</span>
      <span>4820 Meridian Ave. I Suite 600</span>
      <span>Westfield, CA 90417</span>
    </address>
    <address class="contact contact--reach">
      <span>daniel@halloranbrightmoor.com</span>
      <span>www.halloranbrightmoor.com</span>
      <span>T. (855) 410 - 2276</span>
    </address>
  </section>
</body>
</html>
```